Coffee Roaster Needs A Postcard Design

I am coffee roaster ( a home business) and I would like to create a neighborhood delivery service. Once a month I would delivery fresh roasted coffee to my neighbors. I would like to create a postcard to advertise the coffee delivery service.

Preferences: The postcard would be very simple, primarily black and white ( a little color) with visuals; fresh roasted coffee beans, delivered to the doorstep, a great cup of coffee. Simple steps, 1 2 & 3.

I have a website the postcard advertisement should flow with the site : www.brambledgebeanworks.com

Target Market(s)

Upper class residential neighborhood

Industry/Entity Type

Business

Font styles to use
Serif

Colors
f04a50

Requirements
Must have
• Images _ Coffee Beans

```html
<!DOCTYPE html>
<html lang="en">
<head>
<meta charset="utf-8">
<title>Brambledge Bean Works – 3 simple steps to great coffee</title>
<link href="https://fonts.googleapis.com/css2?family=Roboto:wght@300;500;700&display=swap" rel="stylesheet">
<style>
  :root {
    --paper-light: #ece4d3;
    --paper-mid: #d8cbb0;
    --paper-dark: #a8977a;
    --ink: #1f1c19;
    --icon: #2c2924;
    --rule: rgba(60, 50, 40, 0.18);
    --bean-dark: #2a1a10;
    --bean-mid: #5a3a24;
  }
  * { margin: 0; padding: 0; box-sizing: border-box; }
  html, body { width: 1200px; height: 960px; overflow: hidden; }
  body { font-family: "Roboto", Arial, sans-serif; color: var(--ink); }

  .postcard {
    position: relative;
    width: 1200px;
    height: 960px;
    overflow: hidden;
    background:
      radial-gradient(ellipse 55% 45% at 38% 42%, var(--paper-light) 0%, rgba(236,228,211,0) 70%),
      radial-gradient(ellipse 90% 90% at 45% 50%, var(--paper-mid) 30%, var(--paper-dark) 100%);
  }

  .beans-photo {
    position: absolute;
    top: 0; right: 0;
    width: 300px; height: 960px;
    background: linear-gradient(90deg, rgba(90,58,36,0) 0%, rgba(90,58,36,0.55) 30%, var(--bean-mid) 55%, var(--bean-dark) 100%);
  }

  .headline {
    position: absolute;
    left: 101px; top: 130px;
    font-size: 47px;
    font-weight: 300;
    letter-spacing: 2.5px;
    white-space: nowrap;
    color: #3a3530;
  }
  .headline strong { font-weight: 500; color: var(--ink); }

  .step-icon { position: absolute; fill: var(--icon); }
  .icon-beans { left: 167px; top: 262px; width: 107px; height: 102px; }
  .icon-door { left: 750px; top: 398px; width: 78px; height: 148px; }
  .icon-cup { left: 148px; top: 574px; width: 126px; height: 126px; }

  .step-label {
    position: absolute;
    font-size: 24px;
    font-weight: 700;
    letter-spacing: 3.3px;
    white-space: nowrap;
    line-height: 1;
  }
  .step-beans { left: 324px; top: 308px; }
  .step-delivery { left: 192px; top: 457px; }
  .step-enjoy { left: 317px; top: 640px; }

  .divider {
    position: absolute;
    left: 769px; top: 574px;
    width: 121px; height: 1px;
    background: var(--rule);
  }

  .footer {
    position: absolute;
    left: 216px; top: 810px;
    font-size: 19px;
    letter-spacing: 2.4px;
    white-space: nowrap;
  }
  .footer .prompt { font-weight: 300; color: #3a3530; margin-right: 30px; }
  .footer .site { font-weight: 700; color: var(--ink); }
</style>
</head>
<body>
<main class="postcard">
  <div class="beans-photo" role="img" aria-label="Photograph of dark roasted coffee beans piled along the right edge"></div>

  <h1 class="headline">3 simple steps <strong>to great coffee</strong></h1>

  <svg class="step-icon icon-beans" viewBox="0 0 107 102" aria-hidden="true">
    <g transform="rotate(-20 32 26)">
      <ellipse cx="32" cy="26" rx="30" ry="21"/>
      <path d="M4 28 C20 18 40 36 60 24" stroke="#d8cbb0" stroke-width="4" fill="none"/>
    </g>
    <g transform="rotate(-60 85 28)">
      <ellipse cx="85" cy="28" rx="27" ry="19"/>
      <path d="M60 30 C74 20 94 38 111 26" stroke="#d8cbb0" stroke-width="4" fill="none"/>
    </g>
    <g transform="rotate(-30 50 76)">
      <ellipse cx="50" cy="76" rx="29" ry="21"/>
      <path d="M23 78 C38 68 60 86 78 74" stroke="#d8cbb0" stroke-width="4" fill="none"/>
    </g>
  </svg>
  <p class="step-label step-beans">FRESH ROASTED COFFEE BEANS</p>

  <p class="step-label step-delivery">DELIVERED TO YOUR DOORSTEP</p>
  <svg class="step-icon icon-door" viewBox="0 0 78 148" aria-hidden="true">
    <path d="M10 18 L66 4 Q74 2 74 10 L74 138 Q74 146 66 144 L10 130 Q3 128 3 121 L3 27 Q3 20 10 18 Z" fill="none" stroke="var(--icon)" stroke-width="5"/>
    <rect x="10" y="28" width="46" height="102" rx="2"/>
  </svg>

  <div class="divider"></div>

  <svg class="step-icon icon-cup" viewBox="0 0 126 126" aria-hidden="true">
    <g fill="none" stroke="var(--icon)" stroke-width="3.5" stroke-linecap="round">
      <path d="M52 40 c-6 -6 6 -10 0 -16 c-6 -6 6 -10 0 -16"/>
      <path d="M64 40 c-6 -6 6 -10 0 -16 c-6 -6 6 -10 0 -16"/>
      <path d="M76 40 c-6 -6 6 -10 0 -16 c-6 -6 6 -10 0 -16"/>
    </g>
    <path d="M10 50 H102 V64 H110 a16 16 0 0 1 0 32 H97 Q88 106 72 106 H40 Q14 106 10 80 Z M102 72 V88 H108 a8 8 0 0 0 0 -16 Z"/>
    <path d="M0 110 H124 Q118 124 100 124 H24 Q6 124 0 110 Z"/>
  </svg>
  <p class="step-label step-enjoy">ENJOY A GREAT CUP OF COFFEE</p>

  <p class="footer"><span class="prompt">FIND OUT MORE</span><span class="site">BRAMBLEDGEBEANWORKS.COM</span></p>
</main>
</body>
</html>
```